Halcyon Surgery Center Flyer
Flyer for Referring Doctors
Project: Halcyon Surgery Center Flyer
Halcyon Surgery Center Flyer - Health
Creative Brief
Health
Referring doctors to hand to their patients so that they know where there surgery will be performed. We want the patients to feel confident that the surgery center is accredited, professional, and MODERN.
Flyer should have a great modern and crisp image. Clean. Please refer to our website: halcyoncosmeticcarevt.com. I would like to use the images of our office (I can upload these images for your development.). I want a soft, modern, and creative design on the flyer . The patients need a quick beautiful reference of where they are going to surgery. We provide them a seperate packet on all the details. This should be the awe factor flyer.

```html
<!DOCTYPE html>
<html lang="en">
<head>
<meta charset="utf-8">
<title>Halcyon Surgery Center – Flyer for Referring Doctors</title>
<link rel="stylesheet" href="https://fonts.googleapis.com/css2?family=Oswald:wght@300;400;500&family=Lato:wght@400;700&family=Great+Vibes&display=swap">
<style>
  :root {
    --bg: #dcdcdc;
    --brown-dark: #4a3608;
    --brown: #6a4f12;
    --brown-light: #7d5f1a;
    --gold: #e3a51f;
    --gold-soft: #d8ad55;
    --cream: #f4ead2;
    --white: #ffffff;
    --photo-warm: #8a6a3a;
    --photo-deep: #2c2114;
    --photo-blue: #2f5f8c;
  }
  * { box-sizing: border-box; margin: 0; padding: 0; }
  html, body { width: 1200px; height: 904px; overflow: hidden; }
  body { background: var(--bg); font-family: "Lato", sans-serif; position: relative; }

  .flyer {
    position: absolute; left: 80px; width: 1040px; height: 410px;
    background: radial-gradient(ellipse at 40% 40%, var(--brown-light), var(--brown) 55%, var(--brown-dark));
    box-shadow: 0 6px 18px rgba(0,0,0,.25);
  }
  .flyer::after {
    content: ""; position: absolute; inset: 10px;
    border: 1px solid var(--gold-soft); opacity: .55; pointer-events: none;
  }
  .flyer--front { top: 27px; }
  .flyer--back { top: 467px; }

  .brand { position: absolute; display: flex; align-items: center; gap: 12px; }
  .brand__dot { width: 34px; height: 34px; border-radius: 50%; background: var(--gold); flex: none; }
  .brand__name { font-family: "Oswald", sans-serif; font-weight: 400; color: var(--gold); font-size: 22px; letter-spacing: 2px; text-transform: uppercase; line-height: 1.05; }
  .brand__tag { font-size: 11px; color: var(--cream); letter-spacing: 1.5px; text-transform: uppercase; margin-top: 3px; }

  .photo { position: absolute; border: 3px solid var(--gold); }

  /* front */
  .front__brand { left: 40px; top: 40px; }
  .front__title { position: absolute; left: 40px; top: 118px; font-family: "Oswald", sans-serif; font-weight: 300; font-size: 58px; color: var(--white); letter-spacing: 1px; }
  .front__locations-head { position: absolute; left: 40px; top: 222px; font-family: "Oswald", sans-serif; font-weight: 300; font-size: 34px; color: var(--gold); }
  .locations { position: absolute; left: 40px; top: 282px; display: flex; gap: 70px; }
  .location { font-size: 14px; line-height: 1.55; color: var(--cream); }
  .front__cover { left: 700px; top: 32px; width: 180px; height: 240px; background: linear-gradient(160deg, var(--photo-blue), #1d3550); }
  .front__thumb { left: 895px; width: 110px; height: 112px; background: linear-gradient(135deg, var(--photo-warm), var(--photo-deep)); }
  .front__thumb--one { top: 32px; }
  .front__thumb--two { top: 160px; }
  .contact { position: absolute; left: 700px; top: 300px; font-size: 15px; line-height: 1.7; color: var(--cream); }
  .contact strong { color: var(--gold); font-weight: 700; }

  /* back */
  .back__main { left: 24px; top: 24px; width: 600px; height: 362px; background: radial-gradient(ellipse at 50% 30%, #c9a266, var(--photo-warm) 45%, var(--photo-deep)); }
  .back__side { left: 650px; top: 24px; width: 366px; height: 170px; background: linear-gradient(120deg, #a98a5c, var(--photo-deep)); }
  .back__brand { left: 650px; top: 212px; }
  .back__brand .brand__name { font-size: 18px; }
  .back__text { position: absolute; left: 650px; top: 260px; width: 366px; font-size: 12.5px; line-height: 1.5; color: var(--cream); }
  .back__script { position: absolute; left: 650px; top: 354px; width: 366px; font-family: "Great Vibes", cursive; font-size: 28px; color: var(--gold); }
</style>
</head>
<body>

<section class="flyer flyer--front">
  <div class="brand front__brand">
    <span class="brand__dot"></span>
    <div>
      <div class="brand__name">Halcyon Surgery Center</div>
      <div class="brand__tag">Cosmetic &amp; Reconstructive Care</div>
    </div>
  </div>

  <h1 class="front__title">Flyer for Referring Doctors</h1>
  <h2 class="front__locations-head">Our Locations</h2>

  <div class="locations">
    <p class="location">1420 Larkspur Road<br>Suite 200<br>Brambury, VT 05401<br>802-555-0142</p>
    <p class="location">38 Millbrook Avenue<br>Suite 5<br>Weston Falls, VT 05402<br>802-555-0187</p>
  </div>

  <div class="photo front__cover" role="img" aria-label="Magazine cover featuring the center's lead surgeon"></div>
  <div class="photo front__thumb front__thumb--one" role="img" aria-label="Photo of the center's reception area"></div>
  <div class="photo front__thumb front__thumb--two" role="img" aria-label="Photo of a treatment room"></div>

  <p class="contact">Visit <strong>halcyoncosmeticcarevt.com</strong><br>Call <strong>802-555-0100</strong></p>
</section>

<section class="flyer flyer--back">
  <div class="photo back__main" role="img" aria-label="Photo of the surgery center's lit hallway and interior"></div>
  <div class="photo back__side" role="img" aria-label="Photo of the modern consultation room"></div>

  <div class="brand back__brand">
    <span class="brand__dot"></span>
    <div>
      <div class="brand__name">Halcyon Surgery Center</div>
      <div class="brand__tag">Cosmetic &amp; Reconstructive Care</div>
    </div>
  </div>

  <p class="back__text">Our accredited surgical suites pair modern technology with a calm, welcoming setting. Board-certified surgeons and a dedicated nursing team guide each patient from arrival to recovery, so you can rest assured your procedure takes place in a safe, private and comfortable facility.</p>

  <p class="back__script">Halcyon Surgery Center of Excellence</p>
</section>

</body>
</html>
```